GraniteLoop. Customer needs to know about us, what services we provide & contact us

We are a waste tire recycling company. Our primary focus is on providing a sustainable and cost effective service focusing on: Waste Tire Management, Hassle Free Scheduling for Tire Collection, Mobile Shredding & Special site cleanup services. GraniteLoop will be producing TDF, Clean Tire Wire & further materials.
Please look at https://quorvalwheel.example
Please look at https://bandimacorp.example

This is the look and feel of what we want

I have attached a word document with our website info.

Target Market(s)

Tire Install Companies. Such as paltonhaul.example. TDF Purchasers such as kevrofuel.example.

Industry/Entity Type

Waste Tire Recycling

Coding

Coded - Design and coding required

Number of Pages Required

3 page

Font styles to use
Other font styles liked:
• Look at our logo

Requirements
Must have
• We need a 3 page setup for About Us, Services & Contact Us. Contact us should be a form them can fill out and submit to us Images that are related to waste tire recycling. Clean, modern, innovative.
Nice to have
• The color and feel of the website should work with our logo that we did with artmarketly
Should not have
• Anything progressive, political or "woke"

```html
<!DOCTYPE html>
<html lang="en">
<head>
<meta charset="utf-8">
<title>GraniteLoop — Waste Tire Recycling</title>
<link rel="stylesheet" href="https://fonts.googleapis.com/css2?family=Montserrat:wght@500;600;700;800&family=Mulish:wght@400;600;700&display=swap">
<style>
:root{
  --green:#119143;
  --green-dark:#0b6e31;
  --black:#0b0b0b;
  --ink:#222;
  --body:#444;
  --muted:#777;
  --white:#fff;
  --star:#f5a623;
  --soft:#f2f2f2;
  --social:#1d73d6;
}
*{box-sizing:border-box;margin:0;padding:0}
html,body{width:1200px;height:4118px;overflow:hidden;background:var(--white)}
body{font-family:'Mulish',sans-serif;color:var(--body);position:relative}
.abs{position:absolute}
.svg-layer{position:absolute;left:0;width:1200px}
.btn{position:absolute;display:flex;align-items:center;justify-content:center;width:152px;height:52px;font-family:'Montserrat',sans-serif;font-weight:600;font-size:13px;letter-spacing:.5px;text-transform:uppercase;text-decoration:none}
.btn--green{background:var(--green);color:var(--white)}
.btn--white{background:var(--white);color:var(--green)}
.photo{position:absolute}

/* header */
.brand{left:165px;top:30px;display:flex;align-items:center;gap:12px}
.brand__mark{width:50px;height:50px;border-radius:50%;background:var(--green)}
.brand__name{font-family:'Montserrat',sans-serif;font-weight:800;font-size:32px;color:var(--green)}
.topbar{top:22px;display:flex;align-items:center;gap:10px;font-size:13px;color:#333}
.nav{left:470px;top:72px;width:730px;height:52px;background:var(--black)}
.nav__active{position:absolute;left:0;top:0;width:160px;height:52px}
.nav a{position:absolute;top:18px;font-family:'Montserrat',sans-serif;font-weight:600;font-size:13px;color:var(--white);text-decoration:none;transform:translateX(-50%)}
.nav .sep{position:absolute;top:17px;color:#555;font-size:13px}

/* hero */
.hero{left:0;top:124px;width:1200px;height:556px;background:linear-gradient(180deg,#6b9bcf 0%,#a9c6e2 30%,#8a8f8c 52%,#262626 70%,#1c1c1c 100%)}
.hero__title{left:0;top:240px;width:1200px;text-align:center;font-family:'Montserrat',sans-serif;font-weight:700;font-size:27px;line-height:37px;color:var(--white)}

/* headings */
.heading{font-family:'Montserrat',sans-serif;font-weight:800;font-size:35px;color:var(--black);text-transform:uppercase}
.heading span{color:var(--green)}
.copy p{font-size:13px;line-height:23px;letter-spacing:.2px;margin-bottom:12px;color:var(--body)}

/* services */
.services__title{left:0;top:1822px;width:1200px;text-align:center;color:var(--white)}
.service{position:absolute;top:1888px;width:205px}
.service__img{width:205px;height:199px}
.service__label{margin-top:20px;text-align:center;font-family:'Montserrat',sans-serif;font-weight:600;font-size:14px;line-height:18px;color:var(--white)}

/* banner */
.banner__title{left:0;top:3016px;width:1200px;text-align:center;font-family:'Montserrat',sans-serif;font-weight:600;font-size:27px;line-height:35px;letter-spacing:.8px;color:var(--white)}

/* testimonials */
.testimonials__title{left:0;top:3384px;width:1200px;text-align:center}
.card{position:absolute;top:3472px;width:252px;height:228px;background:var(--white);box-shadow:0 6px 22px rgba(0,0,0,.10);padding:30px 18px 0 18px}
.card__quote{position:absolute;right:-22px;top:-20px;width:44px;height:44px;border-radius:50%;background:var(--green);color:var(--white);font-family:'Montserrat',sans-serif;font-weight:800;font-size:34px;line-height:58px;text-align:center}
.card__stars{color:var(--star);font-size:13px;letter-spacing:4px}
.card__stars .off{color:#ddd}
.card__text{margin-top:10px;font-size:11.5px;line-height:20px;color:#555}
.card__person{margin-top:22px;display:flex;align-items:center;gap:10px}
.card__avatar{width:44px;height:44px;border-radius:50%;background:#e6f4ea;border:2px solid #d2ead9}
.card__name{font-family:'Montserrat',sans-serif;font-weight:600;font-size:16px;color:var(--green)}
.card__role{font-size:10.5px;color:#666;margin-top:2px}
.dots{left:0;top:3733px;width:1200px;display:flex;justify-content:center;gap:5px}
.dots i{width:8px;height:8px;border-radius:50%;background:#999;display:block}
.dots i.on{background:#444}

/* footer */
.footer-nav a{position:absolute;top:3884px;font-family:'Montserrat',sans-serif;font-weight:600;font-size:13px;color:var(--white);text-decoration:none;transform:translateX(-50%)}
.contact{position:absolute;top:3970px;display:flex;align-items:center;gap:14px;color:var(--white);font-size:13px;line-height:21px}
.contact__icon{width:30px;height:30px;background:var(--white);display:flex;align-items:center;justify-content:center}
.contact strong{font-family:'Montserrat',sans-serif;font-weight:600;font-size:12.5px}
.copyright{left:163px;top:4070px;font-size:12px;color:var(--white)}
.copyright b{font-weight:700}
.social{position:absolute;top:4060px;width:28px;height:28px;background:var(--social)}
</style>
</head>
<body>

<!-- header -->
<div class="abs brand"><span class="brand__mark"></span><span class="brand__name">GraniteLoop</span></div>
<div class="abs topbar" style="left:705px">
  <svg width="26" height="26" viewBox="0 0 26 26"><circle cx="13" cy="13" r="12" fill="none" stroke="#119143" stroke-width="1.5"/><path d="M9 7l3 3-2 2c1 2 2 3 4 4l2-2 3 3-2 2c-5 0-10-5-10-10z" fill="none" stroke="#119143" stroke-width="1.4"/></svg>
  <span>(555)014-2268</span>
</div>
<div class="abs topbar" style="left:866px">
  <svg width="34" height="24" viewBox="0 0 34 24"><path d="M8 4h24v16H8z M8 4l12 9 12-9" fill="none" stroke="#119143" stroke-width="1.5"/><path d="M1 9h5M3 13h4M1 17h5" stroke="#119143" stroke-width="1.5"/></svg>
  <span>info@graniteloop.example</span>
</div>
<nav class="abs nav">
  <svg class="nav__active" viewBox="0 0 160 52"><polygon points="30,0 160,0 130,52 0,52" fill="#119143"/></svg>
  <a href="#" style="left:79px">HOME</a>
  <span class="sep" style="left:154px">/</span>
  <a href="#" style="left:213px">ABOUT US</a>
  <span class="sep" style="left:286px">/</span>
  <a href="#" style="left:361px">SERVICES</a>
  <span class="sep" style="left:433px">/</span>
  <a href="#" style="left:518px">CONTACT US</a>
</nav>

<!-- hero -->
<div class="abs hero" role="img" aria-label="Photo of piled waste tires in a grassy field under a blue sky"></div>
<h1 class="abs hero__title">We Are A Waste Tire Recycling Company,<br>Providing A Sustainable And Cost Effective Service</h1>
<a class="btn btn--green" href="#" style="left:524px;top:334px">Contact Us</a>
<svg class="svg-layer" style="top:600px" height="90" viewBox="0 600 1200 90">
  <polygon points="0,680 1200,658 1200,690 0,690" fill="#fff"/>
  <polygon points="680,656 1200,624 1200,660" fill="#119143"/>
</svg>

<!-- about -->
<div class="photo" style="left:160px;top:765px;width:414px;height:407px;background:linear-gradient(160deg,#4d6b32,#2b2b2b 55%,#c4561f 75%,#333)" role="img" aria-label="Photo of a worker in orange overalls lifting a tire from a pile"></div>
<h2 class="abs heading" style="left:633px;top:778px"><span>About</span> GraniteLoop</h2>
<div class="abs copy" style="left:633px;top:830px;width:405px">
  <p>GraniteLoop is forging the way towards a more sustainable future through scrap tire collection &amp; waste tire recycling.</p>
  <p>You've got a business to run, and we've got you covered. Let us worry about your scrap tire removal so you don't have to.</p>
  <p>Through the use of innovative technologies, we are not only more eco-friendly but able to pass the savings along to our customers.</p>
  <p>Waste Tire Management is a global problem that GraniteLoop aims to resolve. Though our innovative approach to waste tire management, we are focused on resolving environmental concerns head-on. All while giving businesses across the region an opportunity to make a difference for the environment and their bottom line.</p>
</div>
<div class="abs copy" style="left:163px;top:1222px;width:404px">
  <p>Built upon a foundation of innovation, attention to detail, and budget-conscious services, GraniteLoop is at the forefront of pushing the boundaries of what can be achieved through advancing technology. Through our rigorous procedures, environmental commitment we go beyond expectations. GraniteLoop aims to achieve efficiency all while revolutionizing the industry.</p>
  <p>When your company is deciding on used-tire disposal responsibilities you can rest assured that GraniteLoop has your company's interest at its core. Leave the costly equipment, manpower, and output-reducing duties to us. GraniteLoop will help you focus your time where it counts.</p>
  <p>At our heart GraniteLoop's focus is to always better our processes, support our industry, and environment. Here at GraniteLoop we see ourselves as an extension of your team, outdoing competitors on speed, value, and price point.</p>
  <p>Here at GraniteLoop we're making a stand. Are you joining us</p>
</div>
<div class="photo" style="left:623px;top:1226px;width:414px;height:408px;background:linear-gradient(135deg,#1a1a1a,#4a4a4a 50%,#1f1f1f 80%,#8c7a60)" role="img" aria-label="Close-up photo of a stack of new black tires"></div>

<!-- services -->
<svg class="svg-layer" style="top:1725px" height="680" viewBox="0 1725 1200 680">
  <polygon points="0,1784 1200,1728 1200,2345 0,2293" fill="#119143"/>
  <polygon points="0,1731 900,1731 0,1784" fill="#0b0b0b"/>
  <polygon points="0,1725 1200,1725 1200,1728 0,1731" fill="#fff"/>
  <polygon points="330,2300 1200,2340 1200,2400" fill="#0b0b0b"/>
</svg>
<h2 class="abs heading services__title">Our Services</h2>
<div class="service" style="left:160px"><div class="service__img" style="background:linear-gradient(160deg,#9a9a8a,#2a2a2a 60%,#444)" role="img" aria-label="Photo of stacked waste tires"></div><div class="service__label">Waste Tire<br>Management &amp;<br>Recycling</div></div>
<div class="service" style="left:385px"><div class="service__img" style="background:linear-gradient(160deg,#3a3a3a,#6a7a6a 55%,#3f6fb0)" role="img" aria-label="Photo of a gloved hand inspecting a tire tread"></div><div class="service__label">Tire Remediation<br>&amp; Special Tire<br>Clean-Ups</div></div>
<div class="service" style="left:609px"><div class="service__img" style="background:linear-gradient(160deg,#f2f2f2,#cfcfcf 55%,#8a8a8a)" role="img" aria-label="Photo of a laptop showing a scheduling calendar"></div><div class="service__label">Scheduling &amp;<br>Billing</div></div>
<div class="service" style="left:834px"><div class="service__img" style="background:linear-gradient(160deg,#d8cbb8,#8a6a50 55%,#e8e8e8)" role="img" aria-label="Photo of a customer support agent with a headset"></div><div class="service__label">First Rate<br>Customer Support<br>&amp; Service</div></div>
<a class="btn btn--white" href="#" style="left:524px;top:2190px">Contact Us</a>

<!-- products -->
<div class="photo" style="left:161px;top:2403px;width:413px;height:408px;background:linear-gradient(170deg,#3e5a2a,#5a5550 45%,#2a2622 80%,#3a3530)" role="img" aria-label="Photo of large tractor tires beside a heap of shredded tire material"></div>
<h2 class="abs heading" style="left:634px;top:2434px"><span>Our</span> Products</h2>
<div class="abs copy" style="left:634px;top:2488px;width:403px">
  <p>TDF: GraniteLoop seeks to be one of the leading TDF suppliers to the region. This is a product with a wide range of demand from pulp and paper mills, electrical utilities, industrial boilers to cement and asphalt plants our expertly handled tire-derived fuel is being used and receiving high marks for its ever-expanding list of benefits. From driving boiler efficiency to stamping out emissions, GraniteLoop wants to be your TDF supplier offering additional services to include tire pick-up to TDF drop-off we have your back!</p>
</div>
<a class="btn btn--green" href="#" style="left:634px;top:2718px">Contact Us</a>

<!-- banner -->
<div class="abs" style="left:0;top:2880px;width:1200px;height:420px;background:linear-gradient(180deg,#1a2418 0%,#27321f 45%,#3a3a22 70%,#141a12 100%)" role="img" aria-label="Photo of a lone tree in a field at dusk"></div>
<svg class="svg-layer" style="top:2875px" height="510" viewBox="0 2875 1200 510">
  <polygon points="0,2875 1200,2875 1200,2880 0,2885" fill="#fff"/>
  <polygon points="0,2885 720,2883 0,2942" fill="#119143"/>
  <polygon points="0,3264 1200,3292 1200,3385 0,3385" fill="#fff"/>
  <polygon points="300,3271 1200,3292 1200,3376" fill="#119143"/>
</svg>
<h2 class="abs banner__title">GraniteLoop Is Committed To Sustainability And Looking At<br>Your Waste Tires As A Means To Offer Innovation</h2>
<a class="btn btn--green" href="#" style="left:524px;top:3122px">Contact Us</a>

<!-- testimonials -->
<h2 class="abs heading testimonials__title"><span>Client</span> Testimonials</h2>
<div class="card" style="left:168px">
  <div class="card__quote">”</div>
  <div class="card__stars">★★★★<span class="off">★</span></div>
  <p class="card__text">Lorem ipsum dolor sit a consectetuer adipiscing elit, sed diam nonumy nibh euismod tincidunt uret dolore magna aliquam erat volutpat.</p>
  <div class="card__person"><span class="card__avatar"></span><div><div class="card__name">Darren Holloway</div><div class="card__role">Sed Diam Nonumy</div></div></div>
</div>
<div class="card" style="left:464px">
  <div class="card__quote">”</div>
  <div class="card__stars">★★★★<span class="off">★</span></div>
  <p class="card__text">Lorem ipsum dolor sit a consectetuer adipiscing elit, sed diam nonumy nibh euismod tincidunt uret dolore magna aliquam erat volutpat.</p>
  <div class="card__person"><span class="card__avatar"></span><div><div class="card__name">Marla Pennick</div><div class="card__role">Sed Diam Nonumy</div></div></div>
</div>
<div class="card" style="left:767px">
  <div class="card__quote">”</div>
  <div class="card__stars">★★★★<span class="off">★</span></div>
  <p class="card__text">Lorem ipsum dolor sit a consectetuer adipiscing elit, sed diam nonumy nibh euismod tincidunt uret dolore magna aliquam erat volutpat.</p>
  <div class="card__person"><span class="card__avatar"></span><div><div class="card__name">Lydia Strand</div><div class="card__role">Sed Diam Nonumy</div></div></div>
</div>
<div class="abs dots"><i></i><i class="on"></i><i></i><i></i></div>

<!-- footer -->
<svg class="svg-layer" style="top:3795px" height="323" viewBox="0 3795 1200 323">
  <polygon points="0,3860 1200,3800 1200,4118 0,4118" fill="#119143"/>
  <polygon points="0,3806 640,3806 0,3860" fill="#0b0b0b"/>
</svg>
<nav class="footer-nav">
  <a href="#" style="left:391px">HOME</a>
  <a href="#" style="left:509px">ABOUT US</a>
  <a href="#" style="left:642px">SERVICES</a>
  <a href="#" style="left:784px">CONTACT US</a>
</nav>
<div class="contact" style="left:275px">
  <span class="contact__icon"><svg width="14" height="18" viewBox="0 0 14 18"><path d="M7 1a6 6 0 0 0-6 6c0 4 6 10 6 10s6-6 6-10a6 6 0 0 0-6-6z" fill="#119143"/><circle cx="7" cy="7" r="2.2" fill="#fff"/></svg></span>
  <div>123, Lorem ipsum dolor way,<br>consectet, CA 123456</div>
</div>
<div class="contact" style="left:561px">
  <span class="contact__icon"><svg width="16" height="16" viewBox="0 0 16 16"><path d="M3 1l3 3-2 2c1 2 3 4 5 5l2-2 3 3-2 3C6 15 1 10 1 3z" fill="#119143"/></svg></span>
  <div><strong>PHONE</strong><br>(555)014-2268</div>
</div>
<div class="contact" style="left:767px">
  <span class="contact__icon"><svg width="16" height="16" viewBox="0 0 16 16"><path d="M1 7l14-6-5 14-3-5z" fill="#119143"/></svg></span>
  <div><strong>EMAIL</strong><br>info@graniteloop.example</div>
</div>
<p class="abs copyright">Copyright © 2022 <b>GRANITELOOP</b>. All Rights Reserved.</p>
<span class="social" style="left:928px"></span>
<span class="social" style="left:969px"></span>
<span class="social" style="left:1010px"></span>

</body>
</html>
```